Announcement for a New Trauma Therapy Group - Rack Card

I need a two-sided "rack" card that is 4x9 announcing a Women's Trauma and Loss Group. I am a licensed therapist and will be starting this support group for women who have experienced trauma of all kinds. In addition to groups, I offer individual, couples, and family counseling sessions.

I would like to see designs that are soft tones and use colors like muted blues, greens, and sand tones. The final design should communicate hope and healing as well as have a peaceful feel to it.

I would like a picture of a woman's profile from either the side or from behind her. (possibly a contemplative picture on a beach)

I am attaching a picture of myself to go alongside the bio information as well.

On One Side, I need the description of the group and contact info:

Healing the Hurting Heart
Women's Trauma & Loss Group
Led by Licensed Professional Counselor, Joy Belden Crane

10 Week Group
Cost - $35 session
Group size limited to 10 participants

Topics Include:
What is Trauma?
How Trauma Affects Us
Creating a Feeling of Safety
Managing Trauma Triggers
Importance of Self Care
Healthy vs. Unhealthy Coping
Guilt, Shame, and Blame
Victim vs. Victimized
Grieving through Loss
Anger and Forgiveness
Imagining a Better Future

For More Information, Contact:
Joy Belden Crane, LPC, LMFT
(555) 614-3928
joy@brightmeadowcare.example

On Side Two:

Life hurts and does not seem fair. So what do you do when you are faced with an event in your life that knocks you off your feet? It seems no one understands what you are feeling and no one knows just what to say. It is tempting to pull away and isolate or put up a mask and pretend everything is OK.

It is my desire you know that you are not alone! There are others who understand the feelings you are going through and offer a safe place for encouraging support. I want to invite you to embark on a courageous journey of healing where you will not only learn how to "survive" after trauma and loss, but instead, learn that you can once again "thrive"!
- Joy Belden Crane, LPC, LMFT

Joy Belden Crane is a Licensed Professional Counselor and Licensed Marriage and Family Therapist. She is the owner of Still Waters Counseling Services located in Tulsa, OK.

Joy is a trauma survivor herself and understands firsthand the unique challenges that can arise on the journey to healing.

(Include Joy's picture next to bio)

(Attach logo and business information to this side as well.)

Target Market(s)

Women who have gone through a traumatic experience or loss and are hurting emotionally

Industry/Entity Type

Counsellor

Font styles to use
Serif
Script

Colors
fbe7d2
86cfc6
cfeae6
85abd2
cfdeed

Requirements
Must have
• Joy's picture as well as her logo and contact information must be on the card.
• One side of the card should describe the group with the following description:
• "Healing the Hurting Heart"
• Women's Trauma & Loss Group
• Led by Licensed Professional Counselor, Joy Belden Crane
• 10 Week Group
• Cost - $35 session
• Group size limited to 10 participants
• Topics Include:
• What is Trauma?
• How Trauma Affects Us
• Creating a Feeling of Safety
• Managing Trauma Triggers
• Importance of Self Care
• Healthy vs. Unhealthy Coping
• Guilt, Shame, and Blame
• Victim vs. Victimized
• Grieving through Loss
• Anger and Forgiveness
• Imagining a Better Future
• For More Information, Contact:
• Joy Belden Crane, LPC, LMFT
• (555) 614-3928
• joy@brightmeadowcare.example
• On the second side, it must have this note from Joy:
• Life hurts and does not seem fair. So what do you do when you are faced with an event in your life that knocks you off your feet? It seems no one understands what you are feeling and no one knows just what to say. It is tempting to pull away and isolate or put up a mask and pretend everything is OK.
• It is my desire you know that you are not alone! There are others who understand the feelings you are going through and offer a safe place for encouraging support. I want to invite you to embark on a courageous journey of healing where you will not only learn how to "survive" after trauma and loss, but instead, learn that you can once again "thrive"!
• - Joy Belden Crane, LPC, LMFT
• Joy Belden Crane is a Licensed Professional Counselor and Licensed Marriage and Family Therapist. She is the owner of Still Waters Counseling Services located in Tulsa, OK.
• Joy is a trauma survivor herself and understands firsthand the unique challenges that can arise on the journey to healing. In addition to facilitating groups, Joy also offers individual, marriage, and family counseling.
Nice to have
• soft muted colors that are peaceful. Light blues, greens, sand colors would work well. A picture at the top of the card of either a woman or a woman's profile that is hopeful such as a woman sitting at a beach overlooking the ocean.
Should not have
• No harsh or bright bold colors. This card needs to have a peaceful feeling to it.

```html
<!DOCTYPE html>
<html lang="en">
<head>
<meta charset="utf-8">
<title>Healing the Hurting Heart – Rack Card</title>
<link href="https://fonts.googleapis.com/css2?family=Great+Vibes&family=Lato:wght@300;400&family=Montserrat:wght@400;500;600&family=Oswald:wght@300&display=swap" rel="stylesheet">
<style>
  :root{
    --backdrop:#676767;
    --teal:#86cfc6;
    --teal-light:#cfeae6;
    --blue:#85abd2;
    --blue-light:#cfdeed;
    --sand:#fbe7d2;
    --green:#4a8a2c;
    --ink:#222629;
    --frame:#7aa3ad;
    --white:#ffffff;
  }
  *{box-sizing:border-box;margin:0;padding:0}
  html,body{width:1200px;height:1200px;overflow:hidden}
  body{background:var(--backdrop);font-family:'Montserrat',sans-serif;color:var(--ink);position:relative}
  .card{position:absolute;top:127px;width:420px;height:945px;overflow:hidden;background:var(--white)}
  .card--front{left:150px}
  .card--back{left:630px;background:linear-gradient(180deg,#d6ebf4 0%,#e4f4f6 40%,#d9f0f0 100%)}
  .abs{position:absolute}

  /* front */
  .hero-photo{left:0;top:0;width:420px;height:370px;
    background:linear-gradient(180deg,#d7e6f1 0%,#e9f1f6 50%,#9fb6bf 72%,#7f9ba3 86%,#c9b8a2 100%)}
  .brand{left:0;width:420px;top:70px;display:flex;align-items:center;justify-content:center;gap:10px}
  .brand__dot{width:26px;height:26px;border-radius:50%;background:var(--green)}
  .brand__name{font-family:'Montserrat',sans-serif;font-weight:500;font-size:21px;color:var(--green);line-height:1.1}
  .curve{left:0;width:420px}
  .title{font-family:'Great Vibes',cursive;font-size:47px;line-height:1;color:#111;white-space:nowrap}
  .title--one{left:60px;top:386px}
  .title--two{left:122px;top:428px}
  .group-lead{left:0;width:420px;top:482px;text-align:center;font-size:14px;font-weight:500;line-height:18px}
  .group-length{left:0;width:420px;top:544px;text-align:center;font-size:21px;font-weight:600;letter-spacing:.5px}
  .cost{left:113px;top:569px;height:25px;display:flex;font-size:17.5px;font-weight:500}
  .cost__label{background:var(--blue);color:var(--white);padding:0 14px;line-height:25px;letter-spacing:.5px}
  .cost__value{background:var(--teal-light);padding:0 8px 0 10px;line-height:25px}
  .group-size{left:0;width:420px;top:600px;text-align:center;font-size:17px;font-weight:500}
  .topics{left:20px;top:640px;width:380px;height:192px;background:var(--teal-light);border:1.5px solid var(--blue);border-radius:5px}
  .topics__label{left:140px;top:627px;background:var(--blue);color:var(--white);font-family:'Lato',sans-serif;font-size:17px;padding:0 10px;height:24px;line-height:24px;border-radius:12px}
  .topics__list{position:absolute;top:14px;list-style:none;font-family:'Lato',sans-serif;font-size:14px;line-height:17px}
  .topics__list li{position:relative;padding-left:17px;margin-bottom:9.5px;white-space:nowrap}
  .topics__list--left li:last-child{white-space:normal}
  .topics__list li::before{content:"";position:absolute;left:2px;top:5px;width:7px;height:7px;border:1px solid var(--blue);border-radius:1px}
  .topics__list li::after{content:"";position:absolute;left:4px;top:5px;width:3px;height:5px;border-right:1.3px solid var(--blue);border-bottom:1.3px solid var(--blue);transform:rotate(40deg)}
  .topics__list--left{left:6px;width:190px}
  .topics__list--right{left:200px;width:176px;border-left:1px solid #a8cfd0;padding-left:6px;font-size:13.6px}
  .contact-heading{font-size:15px;font-weight:600}
  .front-contact-heading{left:0;width:420px;top:840px;text-align:center}
  .footer-band{left:0;top:852px;width:420px;height:93px}
  .front-contact{left:0;width:420px;top:884px;text-align:center;color:var(--white)}
  .front-contact__name{font-size:15px;font-weight:400}
  .front-contact__name b{font-weight:600}
  .contact-line{display:flex;align-items:center;gap:5px;font-size:13.5px;color:var(--white)}
  .front-contact .contact-lines{display:flex;justify-content:center;gap:10px;margin-top:5px}
  .icon{width:11px;height:11px;flex:none}

  /* back */
  .note{left:26px;top:31px;width:370px;height:274px;border:1.5px solid var(--frame);border-radius:8px;background:rgba(255,255,255,.28);padding:13px 8px 0 8px}
  .note p{font-size:12.3px;line-height:15.8px;text-align:justify;margin-bottom:12px}
  .note__sign{text-align:right;font-size:12.3px;margin-top:-2px}
  .note__sign i{font-style:italic}
  .quote-mark{font-family:Georgia,serif;font-size:56px;line-height:1;color:var(--blue);font-weight:700}
  .quote-mark--open{left:34px;top:10px;background:#d9edf4;padding:0 4px;height:26px;overflow:hidden;line-height:50px}
  .quote-mark--close{left:352px;top:294px;background:#dcf0f3;padding:0 4px;height:28px;overflow:hidden;line-height:50px}
  .bio{left:33px;top:330px;width:355px;z-index:2}
  .bio p{font-size:11.8px;line-height:15.5px;text-align:justify;margin-bottom:10px}
  .bio-photo{left:0;top:456px;width:420px;height:254px;
    background:linear-gradient(180deg,#8aa08b 0%,#b6b19f 25%,#bcb4a8 50%,#a69d92 100%)}
  .back-brand{left:40px;top:740px;display:flex;align-items:center;gap:8px}
  .back-brand .brand__dot{width:20px;height:20px}
  .back-brand .brand__name{font-size:16px}
  .divider{left:208px;top:718px;width:1px;height:90px;background:#9fc6c4}
  .credentials{left:225px;top:722px}
  .credentials__name{font-family:'Oswald',sans-serif;font-weight:300;font-size:22px;letter-spacing:-.3px;color:#111;margin-bottom:6px;white-space:nowrap}
  .credentials ul{list-style:none}
  .credentials li{position:relative;padding-left:16px;font-size:13.5px;line-height:16px;color:var(--green);margin-bottom:10px}
  .credentials li::before{content:"";position:absolute;left:2px;top:5px;width:5px;height:5px;border-radius:50%;background:var(--blue)}
  .back-contact-heading{left:153px;top:840px;z-index:2}
  .portrait{left:30px;top:815px;width:112px;height:112px;border-radius:50%;border:4px solid var(--teal-light);
    background:radial-gradient(circle at 50% 45%,#e3c9a4 0%,#d2a85e 55%,#6d8a4a 100%);box-shadow:0 0 0 2px var(--teal)}
  .back-contact{left:160px;top:888px}
  .back-contact .contact-line{margin-bottom:8px;gap:9px}
</style>
</head>
<body>

<section class="card card--front" aria-label="Front of rack card">
  <div class="abs hero-photo" role="img" aria-label="Photo: woman seen from behind, sitting on a beach rock looking out over a calm sea under a soft sky"></div>
  <div class="abs brand"><span class="brand__dot"></span><span class="brand__name">Still Waters<br>Counseling</span></div>
  <svg class="abs curve" style="top:326px" width="420" height="60" viewBox="0 0 420 60">
    <path d="M0 28 Q210 2 420 32 L420 60 L0 60Z" fill="var(--white)"/>
    <path d="M0 22 Q210 -6 420 30 L420 32 Q210 4 0 32Z" fill="var(--teal)"/>
  </svg>

  <div class="abs title title--one">Healing the</div>
  <div class="abs title title--two">Hurting Heart</div>
  <div class="abs group-lead">Women's Trauma &amp; Loss Group Led by<br>Licensed Professional Counselor,<br>Joy Belden Crane</div>
  <div class="abs group-length">10 WEEK GROUP</div>
  <div class="abs cost"><span class="cost__label">COST</span><span class="cost__value">$35 session</span></div>
  <div class="abs group-size">Group size limited to 10 participants</div>

  <div class="abs topics">
    <ul class="topics__list topics__list--left">
      <li>What is Trauma?</li>
      <li>How Trauma Affects Us</li>
      <li>Creating a Feeling of Safety</li>
      <li>Managing Trauma Triggers</li>
      <li>Importance of Self Care</li>
      <li>Healthy vs. Unhealthy Coping</li>
    </ul>
    <ul class="topics__list topics__list--right">
      <li>Guilt, Shame, and Blame</li>
      <li>Victim vs. Victimized</li>
      <li>Grieving through Loss</li>
      <li>Anger and Forgiveness</li>
      <li>Imagining a Better Future</li>
    </ul>
  </div>
  <div class="abs topics__label">Topics Include:</div>

  <div class="abs contact-heading front-contact-heading">For More Information, Contact:</div>
  <svg class="abs footer-band" width="420" height="93" viewBox="0 0 420 93">
    <path d="M0 12 Q210 22 420 4 L420 93 L0 93Z" fill="var(--blue)"/>
    <path d="M0 4 Q210 24 420 0 L420 5 Q210 26 0 13Z" fill="var(--teal)"/>
  </svg>
  <div class="abs front-contact">
    <div class="front-contact__name"><b>Joy Belden Crane</b>, LPC, LMFT</div>
    <div class="contact-lines">
      <span class="contact-line"><svg class="icon" viewBox="0 0 12 12"><path d="M2.5 1 L4.5 1 L5 3.8 L3.8 4.8 Q5 7.2 7.2 8.2 L8.2 7 L11 7.5 L11 9.5 Q10.5 11 9 11 Q1 10 1 3 Q1 1.5 2.5 1Z" fill="currentColor"/></svg>(555) 614-3928</span>
      <span class="contact-line"><svg class="icon" viewBox="0 0 12 12"><rect x="1" y="2.5" width="10" height="7" fill="currentColor"/><path d="M1 2.5 L6 6.5 L11 2.5" fill="none" stroke="var(--blue)" stroke-width="1"/></svg>joy@brightmeadowcare.example</span>
    </div>
  </div>
</section>

<section class="card card--back" aria-label="Back of rack card">
  <div class="abs note">
    <p>Life hurts and does not seem fair.&nbsp; So what do you do when you are faced with an event in your life that knocks you off your feet? It seems no one understands what you are feeling and no one knows just what to say. It is tempting to pull away and isolate or put up a mask and pretend everything is OK.</p>
    <p>It is my desire you know that you are not alone! There are others who understand the feelings you are going through and offer a safe place for encouraging support.&nbsp; I want to invite you to embark on a courageous journey of healing where you will not only learn how to "survive" after trauma and loss, but instead, learn that you can once again "thrive"!</p>
    <div class="note__sign">- <b>Joy Belden Crane</b>, <i>LPC, LMFT</i></div>
  </div>
  <div class="abs quote-mark quote-mark--open">&ldquo;</div>
  <div class="abs quote-mark quote-mark--close">&rdquo;</div>

  <div class="abs bio">
    <p>Joy Belden Crane is a Licensed Professional Counselor and Licensed Marriage and Family Therapist.&nbsp; She is the owner of Still Waters Counseling Services located in Tulsa, OK.</p>
    <p>Joy is a trauma survivor herself and understands firsthand the unique challenges that can arise on the journey to healing.</p>
  </div>

  <div class="abs bio-photo" role="img" aria-label="Photo: the counselor sitting on a sandy beach with dunes and wooden stairs behind her"></div>
  <svg class="abs curve" style="top:690px" width="420" height="40" viewBox="0 0 420 40">
    <path d="M0 18 Q210 -2 420 20 L420 40 L0 40Z" fill="var(--white)"/>
    <path d="M0 10 Q210 -6 420 16 L420 21 Q210 -1 0 19Z" fill="var(--teal)"/>
  </svg>
  <div class="abs" style="left:0;top:720px;width:420px;height:140px;background:var(--white)"></div>

  <div class="abs back-brand"><span class="brand__dot"></span><span class="brand__name">Still Waters<br>Counseling</span></div>
  <div class="abs divider"></div>
  <div class="abs credentials">
    <div class="credentials__name">Joy Crane, LPC-S, LMFT</div>
    <ul>
      <li>Licensed Professional<br>Counselor</li>
      <li>Licensed Marriage &amp;<br>family Therapist</li>
    </ul>
  </div>

  <div class="abs contact-heading back-contact-heading">For More Information, Contact:</div>
  <svg class="abs footer-band" style="top:855px" width="420" height="90" viewBox="0 0 420 90">
    <path d="M0 12 Q210 22 420 4 L420 90 L0 90Z" fill="var(--blue)"/>
    <path d="M0 4 Q210 24 420 0 L420 5 Q210 26 0 13Z" fill="var(--teal)"/>
  </svg>
  <div class="abs portrait" role="img" aria-label="Portrait photo of the counselor"></div>
  <div class="abs back-contact">
    <div class="contact-line"><svg class="icon" viewBox="0 0 12 12"><path d="M2.5 1 L4.5 1 L5 3.8 L3.8 4.8 Q5 7.2 7.2 8.2 L8.2 7 L11 7.5 L11 9.5 Q10.5 11 9 11 Q1 10 1 3 Q1 1.5 2.5 1Z" fill="currentColor"/></svg>(555) 614-3928</div>
    <div class="contact-line"><svg class="icon" viewBox="0 0 12 12"><rect x="1" y="2.5" width="10" height="7" fill="currentColor"/><path d="M1 2.5 L6 6.5 L11 2.5" fill="none" stroke="var(--blue)" stroke-width="1"/></svg>joy@brightmeadowcare.example</div>
  </div>
</section>

</body>
</html>
```